Website Design für Reinigungsunternehmen
Zielgruppe
Wir sind ein Reinigungsunternehmen, dass seit 2014 am Markt ist.
Was machen wir:
Das Angebot besteht darin, Räume nach dem IFSG (Infektionsschutzgesetz) und den Richtlinien des Helmut Brandis Instituts mit ausgewählten Verfahren keimfrei zu bekommen.
Hygiene und prophylaktische Desinfektion sind für die Nutzung stark frequentierter Räume und Oberflächen gerade jetzt essentiell, denn die Ausbreitung von Viren und Bakterien kann auch durch präventive Maßnahmen eingedämmt werden.
Das Angebot ist, mit speziellen Reinigungsverfahren in Kombination mit Kaltverneblung ,die Räume fast vollständig von Keimen, Viren und Bakterien zu befreien.
So ist auch die Desinfektion von schwer zugänglichen Stellen und Gegenständen gewährleistet. Die eingesetzte Kaltnebeltechnologie wirkt in Verbindung mit Wasserstoffperoxid in verschiedenen Konzentrationen sowohl bakterizid, viruzid als auch fungizid. Wasserstoffperoxid wird rückstandsfrei abgebaut. Nach einer Einwirkzeit kann der behandelte, desinfizierte Raum sofort mechanisch gelüftet werden – ohne Material oder Umweltschäden zu riskieren.
Hier ein kurzes und erklärendes Video: https://clipvault-demo.de/Qw7TnRpLx2a
Aufgabenstellung
Die Website Soll maximal 3 Seiten haben.. Home (bzw. was wir machen..) Über uns (wer wir sind..) und Kontakt (-daten.
Ich möchte relativ kurz und knapp zum Thema kommen. Wenig Text, nur das wesentliche auf den Punkt gebracht - dafür ein ansprechendes professionelles Design. Bitte keine Bilder mit Gebäude, Reiniger etc. - dafür andere kreative Assoziationen einbringen.

```html
<!DOCTYPE html>
<html lang="de">
<head>
<meta charset="utf-8">
<title>Klarwerk Gebäudereinigung – Leistungen</title>
<link href="https://fonts.googleapis.com/css2?family=Montserrat:wght@400;500;600;700;800&display=swap" rel="stylesheet">
<style>
  :root {
    --navy: #1f3058;
    --sky: #6aaad5;
    --sky-soft: #84b8db;
    --white: #ffffff;
    --paper: #f0f0f0;
    --rule: #d6d6d6;
  }
  * { margin: 0; padding: 0; box-sizing: border-box; }
  html, body { width: 990px; height: 1200px; overflow: hidden; }
  body {
    position: relative;
    background: var(--white);
    font-family: "Montserrat", sans-serif;
    color: var(--navy);
  }

  /* Navigation */
  .main-nav a {
    position: absolute;
    top: 21px;
    height: 25px;
    line-height: 25px;
    font-size: 9.5px;
    font-weight: 600;
    color: var(--navy);
    text-decoration: none;
    transform: translateX(-50%);
  }
  .main-nav .is-active {
    color: var(--sky);
    border: 1.2px solid var(--sky);
    border-radius: 13px;
    padding: 0 8px;
  }

  /* Intro */
  .brand {
    position: absolute;
    left: 193px; top: 104px;
    display: flex; align-items: center; gap: 10px;
  }
  .brand-dot {
    width: 40px; height: 40px; border-radius: 50%;
    background: var(--navy);
  }
  .brand-name {
    font-size: 34px; font-weight: 700; color: var(--navy);
    letter-spacing: -0.5px;
  }
  .intro-title {
    position: absolute; left: 193px; top: 174px;
    font-size: 9px; font-weight: 700;
  }
  .intro-text {
    position: absolute; left: 193px; top: 202px; width: 330px;
    font-size: 8.5px; line-height: 10px; font-weight: 400;
  }

  /* Services band */
  .services {
    position: absolute; left: 0; top: 278px;
    width: 990px; height: 705px;
    background: var(--navy);
  }
  .service-card {
    position: absolute; width: 448px; height: 191px;
    border-radius: 26px;
    background: var(--sky);
    color: var(--white);
    overflow: hidden;
    box-shadow: 0 3px 6px rgba(0,0,0,0.25);
  }
  .service-card.is-light { background: var(--white); color: var(--sky); }
  .service-card .decor {
    position: absolute; right: -10px; top: 70px;
    width: 180px; height: 150px;
    border-radius: 50% 50% 0 0;
    background: radial-gradient(circle at 55% 60%, rgba(255,255,255,0.16), rgba(255,255,255,0) 70%);
  }
  .service-card.is-light .decor {
    background: radial-gradient(circle at 55% 60%, rgba(106,170,213,0.16), rgba(106,170,213,0) 70%);
  }
  .service-icon { position: absolute; left: 21px; top: 17px; width: 34px; height: 34px; }
  .service-title {
    position: absolute; left: 66px; top: 25px;
    font-size: 15.5px; font-weight: 700; white-space: nowrap;
  }
  .service-text {
    position: absolute; left: 67px; top: 66px; width: 226px;
    font-size: 7.9px; line-height: 8.7px;
  }
  .service-text p + p { margin-top: 9px; }
  .service-list {
    position: absolute; left: 309px; top: 67px;
    list-style: none; font-size: 8px;
  }
  .service-list li {
    position: relative; padding-left: 11px; height: 12.6px; line-height: 12px;
  }
  .service-list li::before {
    content: ""; position: absolute; left: 0; top: 3.5px;
    width: 5px; height: 5px; border-radius: 50%;
    background: currentColor;
  }
  .service-back { position: absolute; left: 398px; top: 155px; width: 14px; height: 12px; }

  /* Call to action */
  .cta {
    position: absolute; left: 0; top: 983px; width: 990px; height: 217px;
    background: var(--paper); text-align: center;
  }
  .cta-title {
    position: absolute; left: 0; width: 100%; top: 12px;
    font-size: 56px; font-weight: 800; line-height: 56px; letter-spacing: 0.5px;
  }
  .cta-sub {
    position: absolute; left: 0; width: 100%; top: 62px;
    font-size: 34.5px; font-weight: 700; line-height: 36px; color: var(--sky);
  }
  .cta-phone {
    position: absolute; left: 470px; top: 115px;
    width: 50px; height: 50px; border-radius: 50%;
    background: var(--sky);
  }
  .cta-phone svg { position: absolute; left: 12px; top: 12px; width: 26px; height: 26px; }
  .footer-rule {
    position: absolute; left: 193px; top: 191px; width: 604px; height: 1px;
    background: var(--rule);
  }
  .footer-note {
    position: absolute; left: 0; width: 100%; top: 201px;
    font-size: 6.5px; font-weight: 500;
  }
  .footer-note strong { color: var(--sky); font-weight: 700; }
</style>
</head>
<body>

<nav class="main-nav">
  <a href="#" style="left:393px">HOME</a>
  <a href="#" class="is-active" style="left:483px">LEISTUNGEN</a>
  <a href="#" style="left:587px">KONTAKT</a>
</nav>

<div class="brand">
  <span class="brand-dot"></span>
  <span class="brand-name">Klarwerk</span>
</div>
<h1 class="intro-title">KLARWERK GROUP</h1>
<p class="intro-text">Sed ut perspiciatis unde omnis iste natus error sit voluptatem accusantium doloremque laudantium, totam rem aperiam, eaque ipsa quae ab illo inventore veritatis et quasi architecto beatae vitae dicta sunt explicabo. Nemo enim ipsam voluptatem quia voluptas sit aspernatur aut odit aut fugit, sed quia consequuntur magni dolores eos qui ratione voluptatem sequi nesciunt.</p>

<svg width="0" height="0" style="position:absolute">
  <defs>
    <symbol id="icon-cycle-drop" viewBox="0 0 34 34">
      <path d="M28 9 A13.5 13.5 0 0 0 6 8" fill="none" stroke="currentColor" stroke-width="2"/>
      <path d="M6 25 A13.5 13.5 0 0 0 28 26" fill="none" stroke="currentColor" stroke-width="2"/>
      <path d="M4.5 13 A13.5 13.5 0 0 0 4.5 21" fill="none" stroke="currentColor" stroke-width="2"/>
      <path d="M29.5 21 A13.5 13.5 0 0 0 29.5 13" fill="none" stroke="currentColor" stroke-width="2"/>
      <path d="M25 4 L29.5 9.5 L23 10 Z" fill="currentColor"/>
      <path d="M9 30 L4.5 24.5 L11 24 Z" fill="currentColor"/>
      <path d="M17 9 C19 13 22 16 22 19.5 A5 5 0 0 1 12 19.5 C12 16 15 13 17 9 Z" fill="currentColor"/>
    </symbol>
    <symbol id="icon-arrow-left" viewBox="0 0 14 12">
      <path d="M13 6 H3 M7 1.5 L2 6 L7 10.5" fill="none" stroke="currentColor" stroke-width="2.4" stroke-linecap="round" stroke-linejoin="round"/>
    </symbol>
  </defs>
</svg>

<section class="services">
  <article class="service-card" style="left:194px; top:37px;">
    <div class="decor" role="img" aria-label="Dezente Hintergrundgrafik: Wassertropfen mit Pfeil"></div>
    <svg class="service-icon"><use href="#icon-cycle-drop"/></svg>
    <h2 class="service-title">Flächen- und Raumdesinfektion gem. IFSG § 17</h2>
    <div class="service-text">
      <p>Sed ut perspiciatis unde omnis iste natus error sit voluptatem accusantium doloremque laudantium, totam rem aperiam, eaque ipsa quae ab illo inventore veritatis et quasi architecto beatae vitae dicta sunt explicabo. Nemo enim ipsam voluptatem quia voluptas sit aspernatur aut odit aut fugit, sed quia consequuntur magni dolores eos qui ratione voluptatem sequi nesciunt.</p>
      <p>Neque porro quisquam est, qui dolorem ipsum quia dolor sit amet, consectetur, adipisci velit, sed quia non numquam eius modi tempora incidunt ut labore et dolore magnam aliquam</p>
    </div>
    <ul class="service-list">
      <li>Sed ut perspiciatis</li><li>Voluptatem accusantium</li><li>Neque</li><li>Nemo enim ipsam</li><li>consectetur, adipisci velit</li>
    </ul>
    <svg class="service-back"><use href="#icon-arrow-left"/></svg>
  </article>

  <article class="service-card is-light" style="left:348px; top:253px;">
    <div class="decor" role="img" aria-label="Dezente Hintergrundgrafik: Wassertropfen mit Pfeil"></div>
    <svg class="service-icon"><use href="#icon-cycle-drop"/></svg>
    <h2 class="service-title">Staatlich geprüfte Desinfektoren</h2>
    <div class="service-text">
      <p>Sed ut perspiciatis unde omnis iste natus error sit voluptatem accusantium doloremque laudantium, totam rem aperiam, eaque ipsa quae ab illo inventore veritatis et quasi architecto beatae vitae dicta sunt explicabo. Nemo enim ipsam voluptatem quia voluptas sit aspernatur aut odit aut fugit, sed quia consequuntur magni dolores eos qui ratione voluptatem sequi nesciunt.</p>
      <p>Neque porro quisquam est, qui dolorem ipsum quia dolor sit amet, consectetur, adipisci velit, sed quia non numquam eius modi tempora incidunt ut labore et dolore magnam aliquam</p>
    </div>
    <ul class="service-list">
      <li>Sed ut perspiciatis</li><li>Voluptatem accusantium</li><li>Neque</li><li>Nemo enim ipsam</li><li>consectetur, adipisci velit</li>
    </ul>
    <svg class="service-back"><use href="#icon-arrow-left"/></svg>
  </article>

  <article class="service-card" style="left:194px; top:475px;">
    <div class="decor" role="img" aria-label="Dezente Hintergrundgrafik: Wassertropfen mit Pfeil"></div>
    <svg class="service-icon"><use href="#icon-cycle-drop"/></svg>
    <h2 class="service-title">Staatlich geprüfte Desinfektoren</h2>
    <div class="service-text">
      <p>Sed ut perspiciatis unde omnis iste natus error sit voluptatem accusantium doloremque laudantium, totam rem aperiam, eaque ipsa quae ab illo inventore veritatis et quasi architecto beatae vitae dicta sunt explicabo. Nemo enim ipsam voluptatem quia voluptas sit aspernatur aut odit aut fugit, sed quia consequuntur magni dolores eos qui ratione voluptatem sequi nesciunt.</p>
      <p>Neque porro quisquam est, qui dolorem ipsum quia dolor sit amet, consectetur, adipisci velit, sed quia non numquam eius modi tempora incidunt ut labore et dolore magnam aliquam</p>
    </div>
    <ul class="service-list">
      <li>Sed ut perspiciatis</li><li>Voluptatem accusantium</li><li>Neque</li><li>Nemo enim ipsam</li><li>consectetur, adipisci velit</li>
    </ul>
    <svg class="service-back"><use href="#icon-arrow-left"/></svg>
  </article>
</section>

<section class="cta">
  <h2 class="cta-title">HANDELN SIE JETZT</h2>
  <p class="cta-sub">UND KONTAKTIEREN SIE UNS</p>
  <a class="cta-phone" href="#" aria-label="Anrufen">
    <svg viewBox="0 0 24 24"><path fill="#ffffff" d="M6.6 10.8a15.1 15.1 0 0 0 6.6 6.6l2.2-2.2c.3-.3.7-.4 1-.2 1.1.4 2.3.6 3.6.6.6 0 1 .4 1 1V20c0 .6-.4 1-1 1A17 17 0 0 1 3 4c0-.6.4-1 1-1h3.5c.6 0 1 .4 1 1 0 1.3.2 2.5.6 3.6.1.3 0 .7-.2 1z"/></svg>
  </a>
  <div class="footer-rule"></div>
  <p class="footer-note">ALL RIGHTS RESERVED BY <strong>KLARWERK GROUP</strong></p>
</section>

</body>
</html>
```